Nur Factory, Doner-Kebab, Business Card Design Project

We are a factory of the Doner kebab and distributor for restaurants and supermarkets.
-Try to make the design related to the Business.
-Choose the same colors of the logo (Yellow, red and white).
-Try to make it seriously and high class business.
Target Market(s)
Restaurants, supermarkets and wholesalers companies
Industry/Entity Type
Business

```html
<!DOCTYPE html>
<html lang="en">
<head>
<meta charset="utf-8">
<title>Nur Factory – Business Card</title>
<link rel="stylesheet" href="https://fonts.googleapis.com/css2?family=Open+Sans:wght@400;600;700&display=swap">
<style>
  :root {
    --brand-red: #a81c24;
    --brand-gold: #c9a92c;
    --ink-grey: #555a60;
    --card-white: #ffffff;
    --stage: #eceae6;
  }
  * { box-sizing: border-box; margin: 0; padding: 0; }
  html, body { width: 1200px; height: 900px; overflow: hidden; }
  body {
    background: var(--stage);
    font-family: "Open Sans", Arial, sans-serif;
    display: flex;
    flex-direction: column;
    align-items: center;
    justify-content: center;
    gap: 40px;
  }
  .card {
    position: relative;
    width: 700px;
    height: 400px;
    overflow: hidden;
    box-shadow: 0 6px 18px rgba(0,0,0,.18);
  }

  /* Company name */
  .company {
    position: absolute;
    display: flex;
    align-items: center;
    gap: 12px;
    font-weight: 600;
    font-size: 38px;
    line-height: 1;
  }
  .company__dot {
    width: 16px; height: 16px; border-radius: 50%;
    background: currentColor;
    flex: none;
  }

  /* Back side */
  .card--back { background: var(--brand-red); }
  .card--back .company {
    right: 90px;
    top: 170px;
    color: var(--card-white);
  }

  /* Front side */
  .card--front { background: var(--card-white); }
  .card--front .company {
    left: 40px;
    top: 90px;
    color: var(--brand-red);
  }

  .rule {
    position: absolute;
    left: 40px;
    top: 188px;
    width: 460px;
    height: 2px;
    background: var(--brand-gold);
  }
  .contact {
    position: absolute;
    left: 40px;
    top: 204px;
    list-style: none;
    color: var(--ink-grey);
    font-size: 17px;
    line-height: 25px;
  }
  .contact li { display: flex; align-items: center; gap: 10px; }
  .contact svg { width: 14px; height: 14px; fill: var(--brand-red); flex: none; }

  .person {
    position: absolute;
    right: 40px;
    top: 172px;
    text-align: right;
  }
  .person__name {
    color: var(--brand-red);
    font-weight: 700;
    font-size: 27px;
    line-height: 1.1;
  }
  .person__role { color: var(--ink-grey); font-size: 16px; }
  .address {
    position: absolute;
    right: 40px;
    top: 282px;
    text-align: right;
    color: var(--ink-grey);
    font-size: 17px;
    line-height: 24px;
    font-style: normal;
  }
  .footer-band {
    position: absolute;
    left: 0; bottom: 0;
    width: 700px; height: 40px;
  }
</style>
</head>
<body>

  <section class="card card--back" aria-label="Business card back">
    <div class="company"><span class="company__dot"></span>Nur Factory</div>
  </section>

  <section class="card card--front" aria-label="Business card front">
    <div class="company"><span class="company__dot"></span>Nur Factory</div>

    <div class="rule"></div>

    <ul class="contact">
      <li>
        <svg viewBox="0 0 16 16"><path d="M3.5 1l3 3-1.8 1.8c.8 2 2.5 3.7 4.5 4.5L11 8.5l3 3-2 2.5C6.5 13.5 2.5 9.5 1 3.5z"/></svg>
        (916) 555-0142
      </li>
      <li>
        <svg viewBox="0 0 16 16"><path d="M4 1h8v4H4zM1 6h14v7h-3v2H4v-2H1zM5 10v4h6v-4z"/></svg>
        (916) 555-0143
      </li>
      <li>
        <svg viewBox="0 0 16 16"><path d="M4 0h8a1 1 0 0 1 1 1v14a1 1 0 0 1-1 1H4a1 1 0 0 1-1-1V1a1 1 0 0 1 1-1zm1 2v10h6V2zm3 11a1 1 0 1 0 0 2 1 1 0 0 0 0-2z"/></svg>
        (530) 555-0198
      </li>
      <li>
        <svg viewBox="0 0 16 16"><path d="M0 3h16v1L8 9 0 4zM0 6l8 5 8-5v7H0z"/></svg>
        daniel@nurfactory.com
      </li>
      <li>
        <svg viewBox="0 0 16 16"><path d="M8 0a8 8 0 1 0 0 16A8 8 0 0 0 8 0zm0 2c1 1 1.6 3 1.7 5H6.3C6.4 5 7 3 8 2zM2.1 7h2.2c.1-1.7.5-3.2 1.1-4.3A6 6 0 0 0 2.1 7zm0 2a6 6 0 0 0 3.3 4.3C4.8 12.2 4.4 10.7 4.3 9zm4.2 0h3.4c-.1 2-.7 4-1.7 5-1-1-1.6-3-1.7-5zm5.4 0h2.2a6 6 0 0 1-3.3 4.3c.6-1.1 1-2.6 1.1-4.3zm2.2-2h-2.2c-.1-1.7-.5-3.2-1.1-4.3A6 6 0 0 1 13.9 7z"/></svg>
        www.nurfactory.com
      </li>
    </ul>

    <div class="person">
      <div class="person__name">Daniel Hart</div>
      <div class="person__role">Managing Member</div>
    </div>

    <address class="address">
      2207 Mill Park Road,<br>
      Sacramento, CA 95834
    </address>

    <svg class="footer-band" viewBox="0 0 700 40" preserveAspectRatio="none" aria-hidden="true">
      <rect x="0" y="24" width="400" height="16" fill="var(--brand-gold)"/>
      <path d="M385 40 C395 40 400 14 420 12 L700 10 L700 40 Z" fill="var(--brand-red)"/>
    </svg>
  </section>

</body>
</html>
```